Text only wordpress site to capture emails

Refer to inspiration upload for list of sites that will be useful for you.

We need a site that will be used to capture emails from clients that follow us on social media. The site will be all text, pretty simple. I have a couple of text sites that I like and we can use them for an example.

Menu section will have home, archive, about.
Footer will have © and Website Privacy Policy | Legal and Policies
There will be some text on the home page and an email capture.

This site will be all text no pictures.

I discuss office politics so the text portions will have some questions and answers on this and then prompt for the visitor to subscribe to my email list.

The only purpose of the site is to build an email list from existing social media followers so the site will be pretty simple in and of itself.

• Text only, similar Q&A to uploaded pics.

I will use a template from letter pinecone dotcom for email capture.

I like the simple couriernew font family that is on both sites supplied in the uploads.
• If you use any color it needs to be very minimal.

```html
<!DOCTYPE html>
<html lang="en">
<head>
<meta charset="utf-8">
<title>What The... Newsletter</title>
<link rel="stylesheet" href="https://fonts.googleapis.com/css2?family=Space+Mono:wght@400;700&family=Space+Grotesk:wght@500;700&family=Figtree:wght@400;500;600;700&display=swap">
<style>
  :root {
    --page: #f6f6f6;
    --band: #e6e6e6;
    --ink: #111111;
    --ink-soft: #222222;
    --rule: #808080;
    --panel: #7b7b7b;
    --field: #c8c8c8;
    --white: #ffffff;
  }
  * { margin: 0; padding: 0; box-sizing: border-box; }
  html, body { width: 768px; height: 1200px; overflow: hidden; background: var(--page); }
  body { position: relative; color: var(--ink); font-family: "Figtree", sans-serif; }

  .site-nav { position: absolute; top: 15px; left: 0; width: 768px; height: 20px; }
  .site-nav a {
    position: absolute; top: 0; color: var(--ink); text-decoration: none;
    font-family: "Space Mono", monospace; font-weight: 700; font-size: 12.5px; letter-spacing: 1.6px;
  }

  .hero-title {
    position: absolute; left: 71px; top: 68px;
    font-family: "Space Grotesk", sans-serif; font-weight: 700; font-size: 48px;
    letter-spacing: 10px; line-height: 1;
  }
  .hero-lede { position: absolute; left: 72px; top: 136px; width: 620px; }
  .hero-line {
    display: block; height: 60.5px;
    font-family: "Space Mono", monospace; font-weight: 700; font-size: 26.4px; line-height: 1;
  }
  .hero-line .mark {
    display: inline-block; padding-bottom: 9px;
    border-bottom: 2.5px solid var(--rule);
  }

  .label { position: absolute; top: 434px; font-size: 12.5px; font-weight: 500; letter-spacing: 1px; }
  .email-field {
    position: absolute; left: 72px; top: 480px; width: 221px; height: 24px;
    border-bottom: 1.5px solid var(--field);
    font-size: 12.5px; font-weight: 600; color: var(--field); line-height: 20px;
  }
  .signup-button {
    position: absolute; left: 306px; top: 469px; width: 77px; height: 35px;
    border: 1.5px solid var(--ink); background: transparent;
    font-family: "Space Mono", monospace; font-weight: 700; font-size: 12px;
    display: flex; align-items: center; justify-content: center; color: var(--ink);
  }
  .social-link {
    position: absolute; top: 499px; display: flex; align-items: center; gap: 7px;
    font-family: "Figtree", sans-serif; font-weight: 600; font-size: 12px; color: var(--ink); text-decoration: none;
  }
  .social-link .dot { width: 14px; height: 14px; border: 1.5px solid var(--ink); border-radius: 50%; }

  .experiences { position: absolute; left: 0; top: 586px; width: 768px; height: 535px; background: var(--band); }
  .experiences-title {
    position: absolute; left: 72px; top: 49px;
    font-weight: 700; font-size: 12.5px; letter-spacing: 1.2px; color: var(--ink-soft);
  }
  .faq-row {
    position: absolute; left: 73px; width: 620px; height: 26px;
    border-bottom: 2.5px solid var(--rule);
    display: flex; justify-content: space-between; align-items: flex-start;
  }
  .faq-question { font-family: "Space Grotesk", sans-serif; font-weight: 500; font-size: 20px; letter-spacing: 1.3px; line-height: 22px; color: var(--ink-soft); }
  .faq-toggle { font-family: "Space Mono", monospace; font-weight: 700; font-size: 12.5px; padding-top: 4px; color: var(--ink-soft); }
  .faq-toggle b { margin-left: 6px; font-size: 14px; }

  .faq-open { position: absolute; left: 73px; top: 180px; width: 620px; height: 184px; background: var(--panel); }
  .faq-close { position: absolute; left: 593px; top: 10px; width: 10px; height: 10px; }
  .faq-open-question {
    position: absolute; left: 46px; top: 37px; padding-bottom: 6px;
    border-bottom: 2.5px solid var(--white);
    font-family: "Space Grotesk", sans-serif; font-weight: 500; font-size: 16px; letter-spacing: 0.9px; color: var(--ink-soft);
  }
  .faq-answer {
    position: absolute; left: 47px; top: 88px; width: 525px;
    font-size: 12.4px; line-height: 19.8px; color: var(--ink-soft); letter-spacing: -0.1px;
  }

  .site-footer { position: absolute; left: 0; top: 1121px; width: 768px; height: 79px; }
  .site-footer span, .site-footer a {
    position: absolute; top: 37px; font-size: 9.6px; font-weight: 700; color: var(--ink-soft); text-decoration: none; letter-spacing: 0.2px;
  }
  .site-footer a { padding-bottom: 3px; border-bottom: 1.5px solid var(--rule); }
</style>
</head>
<body>
  <nav class="site-nav">
    <a href="#" style="left:457px">Home</a>
    <a href="#" style="left:537px">Archive</a>
    <a href="#" style="left:647px">About</a>
  </nav>

  <header>
    <h1 class="hero-title">WHAT THE...</h1>
    <p class="hero-lede">
      <span class="hero-line"><span class="mark">Lorem Ipsum is a market newsletter</span></span>
      <span class="hero-line"><span class="mark">to discuss office politics.</span> <span class="mark">Join me</span></span>
      <span class="hero-line"><span class="mark">on ipsum dolor sit amet, consectetur</span></span>
      <span class="hero-line"><span class="mark">adipiscing elit.</span></span>
    </p>
  </header>

  <section class="signup">
    <p class="label" style="left:72px">Get started with my newsletter:</p>
    <div class="email-field">Your Email</div>
    <div class="signup-button">Sign Up</div>
    <p class="label" style="left:500px">Follow me on social:</p>
    <a class="social-link" href="#" style="left:500px"><span class="dot"></span>Photoloop</a>
    <a class="social-link" href="#" style="left:590px"><span class="dot"></span>Friendbook</a>
  </section>

  <section class="experiences">
    <h2 class="experiences-title">UPCOMING EXPERIENCES</h2>
    <div class="faq-row" style="top:96px"><span class="faq-question">Q: why a newsletter?</span><span class="faq-toggle">Details<b>+</b></span></div>
    <div class="faq-row" style="top:137px;left:75px"><span class="faq-question">Q: how are you qualified?</span><span class="faq-toggle">Details<b>+</b></span></div>

    <div class="faq-open">
      <svg class="faq-close" viewBox="0 0 10 10" aria-label="Close">
        <path d="M2 2 L8 8 M8 2 L2 8" stroke="#111" stroke-width="2"/>
      </svg>
      <h3 class="faq-open-question">Q: yours is better?</h3>
      <p class="faq-answer">A: so. what most people don't realize about ETF traders is that they are essentially macro PMs. you touch every asset class: commodities, currencies, equities, rates, even credit. there is no other sell side trading job that even approaches this level of sophistication.</p>
    </div>

    <div class="faq-row" style="top:378px"><span class="faq-question">Q: how much are subscriptions?</span><span class="faq-toggle">Details<b>+</b></span></div>
    <div class="faq-row" style="top:419px"><span class="faq-question">Q: were you a good trader?</span><span class="faq-toggle">Details<b>+</b></span></div>
    <div class="faq-row" style="top:459px"><span class="faq-question">Q: what are your strengths?</span><span class="faq-toggle">Details<b>+</b></span></div>
  </section>

  <footer class="site-footer">
    <span style="left:87px">Copyrigths © 2021. All Rigths Reserved.</span>
    <a href="#" style="left:417px">Privacy Policy</a>
    <a href="#" style="left:582px">Legal And Policies</a>
  </footer>
</body>
</html>
```